Wochen Speiseplan
Zielgruppe
Hospiz
Aufgabenstellung
Wir brauchen für unser Hospiz einen Wochenspeiseplan. Es soll eine Powerpointseite im A4 Format erstellt werden. Wir brauchen 4 unterschiedliche Seiten - für jede Jahreszeit einen Entwurf. Der Speiseplan soll von uns selbst ausgefüllt werden können.
Inhalte: Montag - Sonntag jeweils Mittag- und Abendessen. (Aufgebaut wie ein Stundenplan.). Möglichst große Schriftgröße. In der Fußnote bitte: "Änderungen vorbehalten schreiben". Das ganze soll professionell, aber dennoch liebevoll gestaltet sein. Es soll unseren Bewohnern "Liust machen" draufzuschauen. Der Plan wird jede Woche neu ausgefüllt, ausgedruckt und laminiert. Sollte also einfach zu handhaben sein.
Das Hospiz lebt von Spenden, daher bitte nicht zu aufwendig, dafür aber bezahlbar machen.

```html
<!DOCTYPE html>
<html lang="de">
<head>
<meta charset="utf-8">
<title>Wochen Speiseplan</title>
<link rel="stylesheet" href="https://fonts.googleapis.com/css2?family=Arimo:wght@400;700&family=Open+Sans:wght@400;600&display=swap">
<style>
  :root {
    --page-bg: #f4f1ec;
    --header-blue: #3f8ce0;
    --header-line: #cfe0f5;
    --cell-fill: rgba(255, 255, 255, 0.62);
    --cell-line: rgba(255, 255, 255, 0.85);
    --text-dark: #111111;
    --text-light: #ffffff;
  }
  * { margin: 0; padding: 0; box-sizing: border-box; }
  html, body { width: 1200px; height: 903px; overflow: hidden; background: var(--page-bg); }
  .page { position: relative; width: 1200px; height: 903px; overflow: hidden; }

  .photo { position: absolute; }
  .photo--sandwich { left: 0; top: 0; width: 550px; height: 430px;
    background: linear-gradient(135deg, #c9a27a 0%, #d8c4a6 40%, #e9e2d6 100%); }
  .photo--dessert { left: 550px; top: 0; width: 650px; height: 445px;
    background: linear-gradient(160deg, #efece8 0%, #d9d2cb 55%, #6b4a3a 100%); }
  .photo--pesto-pasta { left: 0; top: 430px; width: 560px; height: 473px;
    background: radial-gradient(ellipse at 45% 65%, #a7b95a 0%, #c9d0b3 40%, #e8e8e4 75%, #d7d9da 100%); }
  .photo--penne { left: 560px; top: 445px; width: 640px; height: 458px;
    background: radial-gradient(ellipse at 60% 55%, #efe2c4 0%, #e4d3ae 45%, #c9b08a 80%, #8fa56a 100%); }
  .photo--beach { left: 75px; top: 151px; width: 1067px; height: 619px;
    background: linear-gradient(180deg, #e8dccb 0%, #cfe3ea 35%, #e6d7bf 55%, #eadfcc 100%); }

  .plan { position: absolute; left: 75px; top: 73px; width: 1067px; height: 697px;
    display: grid; grid-template-columns: repeat(7, 1fr); grid-template-rows: 79px 264px 354px;
    box-shadow: 0 0 10px rgba(0,0,0,0.25); }

  .plan__day { background: var(--header-blue); color: var(--text-light);
    font-family: "Arimo", Arial, sans-serif; font-size: 17px; letter-spacing: 0.2px;
    display: flex; align-items: center; justify-content: center;
    border-right: 1px solid var(--header-line); }
  .plan__day:last-child { border-right: none; }

  .plan__cell { background: var(--cell-fill); border-right: 1px solid var(--cell-line);
    border-top: 1px solid var(--cell-line); position: relative;
    font-family: "Open Sans", Verdana, sans-serif; font-size: 19px; line-height: 24px;
    color: var(--text-dark); text-align: center; }
  .plan__cell:nth-child(7n) { border-right: none; }

  .meal--lunch { position: absolute; left: 0; right: 0; top: 86px; }
  .meal--dinner { position: absolute; left: 0; right: 0; top: 128px; }

  .section-label { position: absolute; left: 75px; width: 1067px; text-align: center;
    font-family: "Arimo", Arial, sans-serif; font-weight: 700; font-size: 18px;
    color: var(--text-dark); letter-spacing: 0.5px; }
  .section-label--lunch { top: 167px; }
  .section-label--dinner { top: 432px; }

  .footnote { position: absolute; right: 60px; top: 845px;
    font-family: "Open Sans", Verdana, sans-serif; font-size: 18px; color: var(--text-dark); }
</style>
</head>
<body>
<div class="page">
  <div class="photo photo--sandwich" role="img" aria-label="Foto eines Club-Sandwiches mit Tomaten und Salat"></div>
  <div class="photo photo--dessert" role="img" aria-label="Foto eines Schokoladendesserts auf weißem Teller mit Gabel"></div>
  <div class="photo photo--pesto-pasta" role="img" aria-label="Foto von Fusilli mit grünem Pesto auf weißem Teller"></div>
  <div class="photo photo--penne" role="img" aria-label="Foto von Penne in heller Sahnesoße mit Basilikum"></div>
  <div class="photo photo--beach" role="img" aria-label="Strandbild mit Muscheln im Sand und Meer"></div>

  <div class="plan">
    <div class="plan__day">MONTAG</div>
    <div class="plan__day">DIENSTAG</div>
    <div class="plan__day">MITTWOCH</div>
    <div class="plan__day">DONNERSTAG</div>
    <div class="plan__day">FREITAG</div>
    <div class="plan__day">SAMSTAG</div>
    <div class="plan__day">SONNTAG</div>

    <div class="plan__cell"><p class="meal--lunch">Pizza Salami<br>mit Salat<br>und Pudding</p></div>
    <div class="plan__cell"><p class="meal--lunch">Pizza Salami<br>mit Salat<br>und Pudding</p></div>
    <div class="plan__cell"><p class="meal--lunch">Pizza Salami<br>mit Salat<br>und Pudding</p></div>
    <div class="plan__cell"><p class="meal--lunch">Pizza Salami<br>mit Salat<br>und Pudding</p></div>
    <div class="plan__cell"><p class="meal--lunch">Pizza Salami<br>mit Salat<br>und Pudding</p></div>
    <div class="plan__cell"><p class="meal--lunch">Pizza Salami<br>mit Salat<br>und Pudding</p></div>
    <div class="plan__cell"><p class="meal--lunch">Pizza Salami<br>mit Salat<br>und Pudding</p></div>

    <div class="plan__cell"><p class="meal--dinner">Gebratene<br>Nudeln mit<br>frischem<br>Gemüse</p></div>
    <div class="plan__cell"><p class="meal--dinner">Gebratene<br>Nudeln mit<br>frischem<br>Gemüse</p></div>
    <div class="plan__cell"><p class="meal--dinner">Gebratene<br>Nudeln mit<br>frischem<br>Gemüse</p></div>
    <div class="plan__cell"><p class="meal--dinner">Gebratene<br>Nudeln mit<br>frischem<br>Gemüse</p></div>
    <div class="plan__cell"><p class="meal--dinner">Gebratene<br>Nudeln mit<br>frischem<br>Gemüse</p></div>
    <div class="plan__cell"><p class="meal--dinner">Gebratene<br>Nudeln mit<br>frischem<br>Gemüse</p></div>
    <div class="plan__cell"><p class="meal--dinner">Gebratene<br>Nudeln mit<br>frischem<br>Gemüse</p></div>
  </div>

  <div class="section-label section-label--lunch">MITTAGS:</div>
  <div class="section-label section-label--dinner">ABENDS:</div>

  <p class="footnote">Änderungen vorbehalten</p>
</div>
</body>
</html>
```